Kelvo Car Audio - Stationary Needed
Business Card, Letterhead, Envelope, Fax Cover, E-mail Signature
Kelvo Car Audio - Stationary Needed -
Creative Brief
Use specific fonts
Designers discretion
Professional
Marcus Feltin
President / CEO
4182 W. Linden Ave. Santa Ana, CA 92817
marc@kelvocaraudio.example
www.kelvocaraudio.example
For business card, use Black background w/ White font.
Would like map of our location, along with the following services we offer: - Car Audio Sales and Installation - Remote Start / Vehicle Security - GPS Navigation - Phone / Wireless Integration - Custom and Pre-Fab Enclosures - Professional Window Tint

```html
<!DOCTYPE html>
<html lang="en">
<head>
<meta charset="utf-8">
<title>Kelvo Car Audio – Stationery</title>
<link href="https://fonts.googleapis.com/css2?family=Roboto:wght@400;700;900&display=swap" rel="stylesheet">
<style>
:root{
  --blue:#5b7fc3;
  --black:#111;
  --grey:#6d6d6d;
  --light:#d9d9d9;
  --paper:#fff;
  --ink:#333;
  --bg:#e6e7e9;
}
*{box-sizing:border-box;margin:0;padding:0}
html,body{width:1200px;height:622px;overflow:hidden}
body{background:var(--bg);font-family:"Roboto",Arial,sans-serif;color:var(--ink);position:relative}
.sheet{position:absolute;background:var(--paper);box-shadow:0 2px 8px rgba(0,0,0,.25)}
.brand{position:absolute;background:var(--black);color:#fff;font-weight:900;display:flex;align-items:center;justify-content:center;white-space:nowrap;letter-spacing:.5px}
.footer-text{position:absolute;left:0;right:0;text-align:center;font-size:6px;line-height:9px;color:var(--grey)}
.band{position:absolute;left:0;right:0;bottom:0;height:9px;background:var(--blue)}
.band::before{content:"";position:absolute;left:0;top:0;bottom:0;width:38%;background:var(--black)}

/* fax cover */
.fax{left:31px;top:72px;width:360px;height:492px}
.fax .brand{right:14px;top:12px;width:110px;height:34px;font-size:11px}
.fax-title{position:absolute;left:14px;top:38px;font-size:30px;line-height:34px;font-weight:900;color:var(--black)}
.fax-fields{position:absolute;left:14px;top:74px;width:332px;display:grid;grid-template-columns:1fr 1fr;column-gap:10px;row-gap:3px}
.field{display:flex;align-items:stretch;height:10px;border-bottom:1px solid var(--light)}
.field-label{width:52px;background:var(--grey);color:#fff;font-size:6px;line-height:10px;padding-left:3px}
.checks{position:absolute;left:14px;top:130px;width:332px;height:14px;background:#ececec;display:flex;justify-content:space-around;align-items:center;font-size:6px}
.checks span::before{content:"";display:inline-block;width:6px;height:6px;border:1px solid var(--grey);margin-right:3px;vertical-align:-1px;background:#fff}
.comments{position:absolute;left:14px;top:152px;font-size:7px}
.fax .footer-text{bottom:20px}

/* letterhead */
.letterhead{left:422px;top:60px;width:315px;height:504px}
.letterhead .brand{right:12px;top:12px;width:100px;height:30px;font-size:10px}
.letterhead .footer-text{bottom:20px}

/* business card front */
.card-front{left:800px;top:48px;width:110px;height:72px;background:#e4e4e4}
.card-front .person{position:absolute;left:8px;top:6px;font-size:5px;line-height:6px;white-space:nowrap}
.card-front .person b{font-size:6px;color:var(--black)}
.card-front .brand{right:0;bottom:8px;width:62px;height:16px;font-size:6px}

/* business card back with map */
.card-back{left:845px;top:163px;width:146px;height:77px;background:var(--blue);color:#fff}
.card-back .services{position:absolute;left:6px;top:7px;font-size:4.3px;line-height:6px;width:76px;white-space:nowrap}
.card-back .services b{font-size:5.5px}
.card-back .map{position:absolute;right:6px;top:8px;width:56px;height:50px;background:linear-gradient(135deg,#f1efe6,#dcd8c8)}

/* disc */
.disc{position:absolute;left:962px;top:15px;width:186px;height:186px}

/* envelope */
.envelope{left:742px;top:288px;width:386px;height:204px}
.envelope .flap{position:absolute;left:0;top:0;width:100%;height:76px}
.envelope .brand{left:16px;top:24px;width:86px;height:26px;font-size:9px}
.envelope .footer-text{bottom:18px}

/* bottom card */
.card-blue{left:809px;top:504px;width:187px;height:79px;background:var(--blue);color:#fff}
.card-blue .brand{left:0;top:22px;width:86px;height:26px;font-size:8.5px}
.card-blue .person{position:absolute;left:96px;top:12px;font-size:5.5px;line-height:7px;white-space:nowrap}
.card-blue .person b{font-size:6.5px}
</style>
</head>
<body>

<section class="sheet fax" aria-label="Fax cover sheet">
  <div class="brand">Kelvo Car Audio</div>
  <h1 class="fax-title">FAX</h1>
  <div class="fax-fields">
    <div class="field"><span class="field-label">To:</span></div>
    <div class="field"><span class="field-label">From:</span></div>
    <div class="field"><span class="field-label">Fax:</span></div>
    <div class="field"><span class="field-label">Pages:</span></div>
    <div class="field"><span class="field-label">Phone:</span></div>
    <div class="field"><span class="field-label">Date:</span></div>
    <div class="field"><span class="field-label">Re:</span></div>
    <div class="field"><span class="field-label">CC:</span></div>
  </div>
  <div class="checks"><span>Urgent</span><span>For Review</span><span>Please Comment</span><span>Please Reply</span><span>Please Recycle</span></div>
  <p class="comments">Comments:</p>
  <p class="footer-text">4182 W. Linden Ave. Santa Ana, CA 92817 · Ph: 714-555-0142 · Fax: 714-555-0143<br>www.kelvocaraudio.example</p>
  <div class="band"></div>
</section>

<section class="sheet letterhead" aria-label="Letterhead">
  <div class="brand">Kelvo Car Audio</div>
  <p class="footer-text">4182 W. Linden Ave. Santa Ana, CA 92817 · Ph: 714-555-0142 · Fax: 714-555-0143<br>www.kelvocaraudio.example</p>
  <div class="band"></div>
</section>

<section class="sheet card-front" aria-label="Business card front">
  <p class="person"><b>Marcus Feltin</b><br>President / CEO<br>4182 W. Linden Ave.<br>Santa Ana, CA 92817<br>Ph: 714-555-0142<br>marc@kelvocaraudio.example</p>
  <div class="brand">Kelvo Car Audio</div>
</section>

<svg class="disc" viewBox="0 0 186 186" aria-label="Disc label">
  <defs><clipPath id="disc-clip"><circle cx="93" cy="93" r="91"/></clipPath></defs>
  <g clip-path="url(#disc-clip)">
    <rect width="186" height="186" fill="var(--blue)"/>
    <rect width="93" height="186" fill="#1c1c1c"/>
    <rect x="0" y="110" width="186" height="34" fill="var(--black)"/>
    <text x="93" y="132" text-anchor="middle" fill="#fff" font-family="Roboto, Arial, sans-serif" font-weight="900" font-size="14">Kelvo Car Audio</text>
  </g>
  <circle cx="93" cy="93" r="91" fill="none" stroke="#bbb" stroke-width="1"/>
  <circle cx="93" cy="93" r="24" fill="#cfd2d6" stroke="#999"/>
  <circle cx="93" cy="93" r="10" fill="var(--bg)" stroke="#999"/>
</svg>

<section class="sheet card-back" aria-label="Business card back">
  <p class="services"><b>Our Services</b><br>Car Audio Sales and Installation<br>Remote Start / Vehicle Security<br>GPS Navigation<br>Phone / Wireless Integration<br>Custom and Pre-Fab Enclosures<br>Professional Window Tint</p>
  <div class="map" role="img" aria-label="Map of the shop location"></div>
</section>

<section class="sheet envelope" aria-label="Envelope">
  <svg class="flap" viewBox="0 0 386 76" preserveAspectRatio="none" aria-hidden="true">
    <path d="M0 0H386V58Q193 84 0 58Z" fill="var(--blue)"/>
  </svg>
  <div class="brand">Kelvo Car Audio</div>
  <p class="footer-text">4182 W. Linden Ave. Santa Ana, CA 92817 · Ph: 714-555-0142<br>www.kelvocaraudio.example</p>
  <div class="band"></div>
</section>

<section class="sheet card-blue" aria-label="Business card">
  <div class="brand">Kelvo Car Audio</div>
  <p class="person"><b>Marcus Feltin</b><br>President / CEO<br>Ph: 714-555-0142<br>marc@kelvocaraudio.example<br>www.kelvocaraudio.example</p>
</section>

</body>
</html>
```